Business Card Design

I need a business card for company that is a limited company that was originally an off-road vehicle company (atv's side by sides snowmobiles and motorcycles) and I have recently sold the assets of the company that was operating under a different name and have become semi retired. I continue to do maintenance on these types of vehicles and also sell and install parts and accessories. Recently I have also contracted to a snowmobile club to operate their groomer to groom the snowmobile trails. I would like bright and bold colors.
Industry/Entity Type
Club
Contact Information for Business Card
KTV Holdings Ltd.
Milo Fenwick
780-413-2769

```html
<!DOCTYPE html>
<html lang="en">
<head>
<meta charset="UTF-8">
<title>KTV Holdings Ltd. – Business Card</title>
<link href="https://fonts.googleapis.com/css2?family=Open+Sans:wght@400;600;700&display=swap" rel="stylesheet">
<style>
  :root {
    --backdrop: #2a2a2b;
    --card-black: #1c1c1d;
    --band-black: #262627;
    --paper: #f6f6f6;
    --orange: #ea9226;
    --ink: #1f1f1f;
  }
  * { margin: 0; padding: 0; box-sizing: border-box; }
  html, body {
    width: 1200px;
    height: 800px;
    overflow: hidden;
    background: var(--backdrop);
    font-family: "Open Sans", Arial, sans-serif;
  }
  .canvas {
    position: relative;
    width: 1200px;
    height: 800px;
  }
  .card {
    position: absolute;
    left: 320px;
    width: 560px;
    height: 320px;
    overflow: hidden;
    box-shadow: 0 10px 30px rgba(0,0,0,0.45);
  }
  .card--back { top: 40px; background: var(--card-black); }
  .card--front { top: 440px; background: var(--paper); }

  .back-name {
    position: absolute;
    inset: 0;
    display: flex;
    align-items: center;
    justify-content: center;
    color: var(--orange);
    font-weight: 700;
    font-size: 40px;
    letter-spacing: 0.5px;
  }

  .stripe-orange {
    position: absolute;
    left: 0; top: 0;
    width: 90px; height: 320px;
    background: var(--orange);
  }
  .band-black {
    position: absolute;
    left: 90px;
    width: 72px;
    background: var(--band-black);
  }
  .band-black--top { top: 0; height: 142px; }
  .band-black--bottom { top: 192px; height: 128px; }

  .front-name {
    position: absolute;
    left: 104px;
    top: 142px;
    height: 50px;
    display: flex;
    align-items: center;
    color: var(--orange);
    font-weight: 700;
    font-size: 40px;
    letter-spacing: 0.5px;
    white-space: nowrap;
  }

  .contact-person {
    position: absolute;
    right: 44px;
    top: 52px;
    text-align: left;
  }
  .person-name {
    color: var(--ink);
    font-weight: 700;
    font-size: 16px;
    line-height: 1.2;
  }
  .person-title {
    color: var(--orange);
    font-weight: 600;
    font-size: 12px;
    line-height: 1.3;
  }
  .phone-tag {
    position: absolute;
    right: 28px;
    top: 104px;
    width: 128px;
    height: 24px;
    background: var(--orange);
    color: var(--ink);
    font-size: 13px;
    font-weight: 400;
    display: flex;
    align-items: center;
    justify-content: center;
  }
</style>
</head>
<body>
  <main class="canvas">
    <section class="card card--back" aria-label="Business card back">
      <div class="back-name">KTV Holdings Ltd.</div>
    </section>

    <section class="card card--front" aria-label="Business card front">
      <div class="stripe-orange"></div>
      <div class="band-black band-black--top"></div>
      <div class="band-black band-black--bottom"></div>

      <div class="contact-person">
        <p class="person-name">Milo Fenwick</p>
        <p class="person-title">Manager</p>
      </div>
      <div class="phone-tag">780-413-2769</div>

      <div class="front-name">KTV Holdings Ltd.</div>
    </section>
  </main>
</body>
</html>
```